Meadowlyn Acres Website Design

We have been redeveloping our website already and are quite happy with the content, but the design needs to be better:
https://harvo-link.example-host.com/

Pages, content, concept etc. Can all be taken from the redeveloped website.
The farmer can register and edit/view their profile, subscribe and these pages need to be designed better as well as contact, about, pricing, tos, privacy and a page with example portlets.

We need a website to appeal to farmers, investors and retiring farmers.

The design should be clean and a little country.

We don't want any repeat designs that some may submit to every project and has no respect for the project brief, so please don't submit them.

Target Market(s)

farmers, investors, retirees

Industry/Entity Type

Farming

Number of Pages Required

5+ page

Colors

Designer to choose colors to be used in the design.

Requirements
Must have
• Nice, clean modern design that is appealing
• Profile page laid out nicely

```html
<!DOCTYPE html>
<html lang="en">
<head>
<meta charset="utf-8">
<title>Meadowlyn Acres</title>
<link href="https://fonts.googleapis.com/css2?family=Jost:wght@300;400;500&display=swap" rel="stylesheet">
<style>
:root{
  --green:#3db54a;
  --green-light:#b9dcb0;
  --slate:#474c54;
  --slate-dark:#3c4148;
  --ink:#2f3236;
  --muted:#7a7d82;
  --white:#ffffff;
  --paper:#f4f4f4;
}
*{box-sizing:border-box;margin:0;padding:0}
html,body{width:1200px;height:4100px;overflow:hidden}
body{font-family:"Jost",sans-serif;color:var(--ink);background:var(--white);font-weight:300}
section,header,footer{position:relative;width:1200px;overflow:hidden}
.photo{position:absolute;inset:0}
.btn{display:inline-block;border:2px solid var(--green);border-radius:22px;padding:8px 30px;font-size:15px;color:var(--white);font-weight:400;text-align:center}
.btn--solid{background:var(--green)}
.btn--dark-text{color:var(--ink)}
.section-title{font-size:34px;font-weight:400;text-align:center;position:relative}
.section-title::after{content:"";display:block;width:44px;height:2px;background:var(--green);margin:8px auto 0}
.brand{display:flex;align-items:center;gap:14px;font-size:22px;font-weight:400;color:var(--white)}
.brand__mark{width:40px;height:40px;border-radius:50%;border:2px solid var(--white)}

/* hero */
.hero{height:552px}
.hero .photo{background:linear-gradient(160deg,#8e8d87 0%,#6c6a5e 35%,#a64138 55%,#7c7a55 75%,#4f5638 100%)}
.hero::before{content:"";position:absolute;inset:0;background:rgba(30,30,30,.28)}
.nav{position:absolute;top:30px;left:56px;right:56px;display:flex;align-items:center;z-index:2}
.nav__links{display:flex;gap:30px;margin-left:50px;font-size:15px;color:var(--white);font-weight:400}
.nav__links .is-active{border-bottom:2px solid var(--green);padding-bottom:3px}
.nav__login{margin-left:auto;margin-right:26px;font-size:15px;color:var(--white);display:flex;align-items:center;gap:8px}
.nav__login i{width:14px;height:14px;border-radius:50%;background:var(--white)}
.hero__copy{position:absolute;top:262px;width:100%;text-align:center;color:var(--white);z-index:2}
.hero__copy h1{font-size:34px;font-weight:300;line-height:1.2}
.hero__copy b{font-weight:500}
.hero__ctas{margin-top:26px;display:flex;justify-content:center;gap:30px}
.hero__down{position:absolute;bottom:22px;left:592px;z-index:2}

/* story */
.story{height:459px;display:flex}
.story__text{width:600px;padding:70px 80px 0 88px;background:var(--white)}
.story__text h2{font-size:32px;font-weight:400}
.story__lead{font-size:16px;margin:4px 0 26px;font-weight:400}
.story__body{font-size:13px;line-height:1.6;color:var(--muted);width:430px}
.story__text .btn{margin-top:50px}
.story__media{position:relative;width:600px}
.story__media .photo{background:linear-gradient(135deg,#5a5348,#8a7b65 45%,#3f3a34)}
.play{position:absolute;left:245px;top:170px}

/* own */
.own{height:569px;padding-top:65px;text-align:center}
.own__sub{width:560px;margin:26px auto 0;font-size:14px;line-height:1.5;color:var(--muted)}
.own__grid{display:flex;justify-content:center;gap:30px;margin-top:40px}
.own__item{width:235px}
.own__circle{width:235px;height:235px;border-radius:50%}
.own__item p{margin-top:22px;font-size:15px;line-height:1.35;color:var(--ink)}

/* works */
.works{height:465px;color:var(--white);text-align:center;padding-top:65px}
.works .photo{background:linear-gradient(180deg,#4a5056 0%,#3e4a3a 60%,#344030 100%)}
.works::before{content:"";position:absolute;inset:0;background:rgba(52,56,62,.55)}
.works > *{position:relative}
.works .section-title{color:var(--white)}
.works__steps{display:flex;justify-content:center;gap:90px;margin-top:55px}
.step{width:250px}
.step__icon{width:100px;height:100px;margin:0 auto;border-radius:8px;background:rgba(255,255,255,.18)}
.step p{font-size:15px;margin:22px 0 24px;line-height:1.35;height:40px}
.step .btn{width:165px}

/* aspiring */
.aspiring{height:437px;padding-top:65px}
.profile{display:flex;gap:50px;margin:55px 0 0 140px}
.profile__photo{width:205px;height:205px;border-radius:50%;background:linear-gradient(140deg,#b84a3b,#6b6f76 50%,#d9a06a)}
.profile__info{width:690px;padding-top:16px}
.profile__info h3{font-size:17px;font-weight:400}
.profile__info p{font-size:13.5px;color:var(--muted);line-height:1.6;margin:8px 0 20px}
.profile__info .btn{padding:7px 22px}
.arrow{position:absolute;top:250px;font-size:22px;color:#9a9da2}

/* split */
.split{height:459px;display:flex}
.split__col{width:600px;padding:70px 88px 0;color:var(--white)}
.split__col h2{font-size:32px;font-weight:400}
.split__col .lead{font-size:15px;line-height:1.35;margin-top:2px}
.subscribe{background:var(--green)}
.field{width:350px;height:36px;border-radius:18px;background:var(--green-light);margin-top:14px;padding:0 22px;font-size:13px;line-height:36px;color:#3c7f42}
.subscribe .field:first-of-type{margin-top:40px}
.join{margin-top:14px;background:var(--slate);border-color:var(--slate);padding:7px 38px}
.note{margin-top:36px;font-size:14px;display:flex;align-items:center;gap:10px}
.note u{color:var(--white)}
.dot{width:14px;height:14px;border-radius:50%;background:var(--white)}
.investors{background:var(--slate)}
.investors .body{font-size:13px;line-height:1.55;margin-top:30px;opacity:.85;width:420px}
.investors .btn{margin-top:30px}

/* quotes */
.quotes{height:462px;padding-top:70px}
.quotes__row{display:flex;justify-content:center;gap:80px;margin-top:50px}
.quote{width:420px;position:relative;padding-left:40px}
.quote::before{content:"\201C";position:absolute;left:0;top:-18px;font-size:64px;color:var(--green);font-weight:400}
.quote p{font-size:14px;line-height:1.55;color:var(--muted)}
.quote__by{margin-top:44px;display:flex;gap:22px}
.quote__by i{width:44px;height:1px;background:var(--ink);margin-top:11px}
.quote__by b{font-weight:400;font-size:15px;display:block}
.quote__by span{font-size:13px;color:var(--muted);display:block;line-height:1.6}
.quote__by em{font-style:normal;font-size:13px;color:var(--muted);display:block;margin-top:12px}

/* retiring */
.retiring{height:369px;color:var(--white);text-align:center;padding-top:70px}
.retiring .photo{background:linear-gradient(180deg,#3e444a 0%,#5c5a4c 55%,#3c3f34 100%)}
.retiring::before{content:"";position:absolute;inset:0;background:rgba(50,54,60,.5)}
.retiring > *{position:relative}
.retiring h2{font-size:32px;font-weight:400}
.retiring p{font-size:16px;line-height:1.35}
.retiring .btn{margin-top:24px;padding:7px 30px}
.retiring .note{justify-content:center;margin-top:30px}

/* footer */
.footer{height:328px;background:var(--slate);color:var(--white)}
.footer__bar{position:absolute;top:70px;left:56px;right:56px;display:flex;align-items:center}
.footer__links{display:flex;gap:24px;margin-left:30px;font-size:14px;font-weight:400}
.footer__links .is-active{color:var(--green)}
.social{margin-left:auto;display:flex;gap:12px;margin-right:34px}
.social i{width:30px;height:30px;border-radius:50%;border:2px solid var(--white)}
.social i.is-on{background:var(--green);border-color:var(--green)}
.footer__up{position:absolute;top:200px;left:590px}
.footer__legal{position:absolute;top:262px;width:100%;text-align:center;font-size:12px;line-height:1.6;opacity:.85}
</style>
</head>
<body>

<header class="hero">
  <div class="photo" role="img" aria-label="Photo of a farming family with young children and a dog in front of a shed"></div>
  <nav class="nav">
    <div class="brand"><span class="brand__mark"></span>Meadowlyn Acres</div>
    <div class="nav__links">
      <span class="is-active">Aspiring Farmers</span><span>Investors</span><span>Retiring Farmer</span><span>Blog</span><span>Pricing</span>
    </div>
    <div class="nav__login"><i></i>Login</div>
    <span class="btn btn--solid">Donate</span>
  </nav>
  <div class="hero__copy">
    <h1>We have the <b>best farmers</b><br>in Australia <b>ready to work</b> with you on your farm.</h1>
    <div class="hero__ctas"><span class="btn">Sign up now!</span><span class="btn">Explore More</span></div>
  </div>
  <svg class="hero__down" width="16" height="10" viewBox="0 0 16 10"><path d="M2 2l6 6 6-6" fill="none" stroke="#fff" stroke-width="2"/></svg>
</header>

<section class="story">
  <div class="story__text">
    <h2>Meadowlyn Acres</h2>
    <p class="story__lead">Meadowlyn Acres began with Rob and Nell Carrow.</p>
    <p class="story__body">Rob and Nell have three daughters and a son and live in Albury NSW. They are aspiring farmers, raising 50 head of cattle on agisted land around the district. Together Rob and Nell have started Carrow Valley Beef, which is a 100% grass fed beef business where they sell direct to customers in the Albury area.</p>
    <span class="btn btn--dark-text">About Us</span>
  </div>
  <div class="story__media">
    <div class="photo" role="img" aria-label="Photo of the founding family standing together outdoors"></div>
    <svg class="play" width="64" height="64" viewBox="0 0 64 64"><circle cx="32" cy="32" r="30" fill="none" stroke="#fff" stroke-width="3"/><path d="M26 20l18 12-18 12z" fill="#fff"/></svg>
  </div>
</section>

<section class="own">
  <h2 class="section-title">You can own a farm</h2>
  <p class="own__sub">We know how hard it is for a young family to find the capital required to own and operate their own farm - so we started Meadowlyn Acres.</p>
  <div class="own__grid">
    <div class="own__item"><div class="own__circle" role="img" aria-label="Photo of a young farming family" style="background:linear-gradient(140deg,#8fa3b8,#c9b79a)"></div><p>We connect a young<br>farming family</p></div>
    <div class="own__item"><div class="own__circle" role="img" aria-label="Photo of a retiring farming couple" style="background:linear-gradient(140deg,#9cc0e0,#c8a58a)"></div><p>With a retiring farming<br>family</p></div>
    <div class="own__item"><div class="own__circle" role="img" aria-label="Photo of investors reviewing documents" style="background:linear-gradient(140deg,#d8dade,#4f5560)"></div><p>And investors</p></div>
    <div class="own__item"><div class="own__circle" role="img" aria-label="Photo of a family walking across a field" style="background:linear-gradient(140deg,#c9b48c,#7e6a4c)"></div><p>To own and operate a farm<br>together</p></div>
  </div>
</section>

<section class="works">
  <div class="photo" role="img" aria-label="Background photo of a farmer working a field"></div>
  <h2 class="section-title">The way it works</h2>
  <div class="works__steps">
    <div class="step"><div class="step__icon" role="img" aria-label="Line icon of a farmer"></div><p>01. Register as an Aspiring<br>Farmer</p><span class="btn">Register</span></div>
    <div class="step"><div class="step__icon" role="img" aria-label="Line icon of a tractor"></div><p>02. Build your farm skills to get<br>yourself farm-ready</p><span class="btn btn--solid">Farm-ready</span></div>
    <div class="step"><div class="step__icon" role="img" aria-label="Line icon of a hay bale"></div><p>03. Together we find you your<br>dream farm</p><span class="btn">Match-Making</span></div>
  </div>
</section>

<section class="aspiring">
  <h2 class="section-title">Aspiring farmers</h2>
  <span class="arrow" style="left:86px">&#8249;</span><span class="arrow" style="right:86px;color:var(--green)">&#8250;</span>
  <div class="profile">
    <div class="profile__photo" role="img" aria-label="Photo of two aspiring farmers cooking in a kitchen"></div>
    <div class="profile__info">
      <h3>Liam Ostry &amp; Dara</h3>
      <p>I really love to farm as farming is forever. I would love to farm anywhere there is an opportunity to live and work in a local farming community. Our family has been raising stock for many years and we are ready ...</p>
      <span class="btn btn--dark-text">View Profile</span>
    </div>
  </div>
</section>

<section class="split">
  <div class="split__col subscribe">
    <h2>Subscribe Us</h2>
    <p class="lead">Join now and receive to either an aspiring or premium<br>farmers</p>
    <div class="field">Your Name</div>
    <div class="field">Enter your Email</div>
    <span class="btn join">Join Now</span>
    <p class="note"><i class="dot"></i>Visit our <u>Pricing Page</u> to find out more ...</p>
  </div>
  <div class="split__col investors">
    <h2>Investors</h2>
    <p class="lead">We have the best farmers in Australia ready to<br>work with you on your farm.</p>
    <p class="body">Simply browse the list and decide who you want to work with. No registration required and your information will be kept private.</p>
    <span class="btn btn--solid">Sign up now!</span>
    <p class="note"><i class="dot"></i>or <u>Find out more</u> ...</p>
  </div>
</section>

<section class="quotes">
  <h2 class="section-title">What our farmers say?</h2>
  <span class="arrow" style="left:86px;top:310px">&#8249;</span><span class="arrow" style="right:86px;top:310px">&#8250;</span>
  <div class="quotes__row">
    <div class="quote">
      <p>Land access is a major barrier to growing more farmers, and we are really excited to see the development of things like Meadowlyn Acres - creative ways to assist young or emerging farmers onto land!</p>
      <div class="quote__by"><i></i><div><b>Petra Vanek,</b><span>Wattlebrook Farms</span><em>Daylesford Victoria</em></div></div>
    </div>
    <div class="quote">
      <p>Meadowlyn Acres can offer an opportunity to put people with the skills and ambition, with either a farming family looking to transition into retirement or for some one who doesn't have the skills but has capital and wants somewhere safe to invest.</p>
      <div class="quote__by"><i></i><div><b>Callum Brae,</b><span>Aspiring Farmer</span><em>Daylesford Victoria</em></div></div>
    </div>
  </div>
</section>

<section class="retiring">
  <div class="photo" role="img" aria-label="Background photo of farmers working a field at dusk"></div>
  <h2>Retiring Farmers</h2>
  <p>Are you looking for a positive way to step back from your farm?<br>Get in touch discuss the best farm succession opportunity for you</p>
  <span class="btn">Enquire Now</span>
  <p class="note"><i class="dot"></i>or <u>Find out more</u> ...</p>
</section>

<footer class="footer">
  <div class="footer__bar">
    <div class="brand"><span class="brand__mark"></span>Meadowlyn Acres</div>
    <div class="footer__links"><span>Farmers</span><span class="is-active">Investors</span><span>Retiring</span><span>About</span><span>Pricing</span><span>Newsletter</span></div>
    <div class="social"><i></i><i class="is-on"></i><i></i></div>
    <span class="btn btn--solid">Donate</span>
  </div>
  <svg class="footer__up" width="20" height="24" viewBox="0 0 20 24"><path d="M10 22V3M3 10l7-7 7 7" fill="none" stroke="#fff" stroke-width="2"/></svg>
  <p class="footer__legal">&copy; Meadowlyn Acres 2017.<br>Terms of Service &nbsp;/&nbsp; Privacy &nbsp;/&nbsp; Contact Us</p>
</footer>

</body>
</html>
```